Design some Business Cards for QR-TOP

I have a logo that I am pleased with, but it needs to be sharpened up. I would like to use the refined logo for business cards and packaging. I have a new product that I am going to do market research on and decide if the market will allow me to pursue it further. If things go right I will build a website. I would like to keep the business cards, packaging, and website very similar.

```html
<!DOCTYPE html>
<html lang="en">
<head>
<meta charset="utf-8">
<title>QR-TOP Business Cards</title>
<link href="https://fonts.googleapis.com/css2?family=Open+Sans:wght@400;600&display=swap" rel="stylesheet">
<style>
  :root{
    --stage:#000000;
    --card:#2b2a2b;
    --accent:#ea1f2b;
    --ink:#ffffff;
    --muted:#d9d9d9;
    --rule:#6a6a6a;
  }
  *{margin:0;padding:0;box-sizing:border-box}
  html,body{width:1200px;height:675px;overflow:hidden;background:var(--stage)}
  body{font-family:"Open Sans",Arial,sans-serif;color:var(--ink);position:relative}
  .card{
    position:absolute;top:188px;width:520px;height:300px;
    background:var(--card);border:7px solid var(--accent);
  }
  .card--front{left:60px}
  .card--back{left:620px}
  .brand-name{
    font-family:"Open Sans",Arial,sans-serif;font-weight:600;
    color:var(--ink);line-height:1;letter-spacing:1px;white-space:nowrap;
  }
  .card--front .brand-name{position:absolute;top:62px;left:206px;font-size:40px}
  .holder{position:absolute;top:54px;left:0;padding-left:24px}
  .holder__marker{position:absolute;left:0;top:0;width:10px;height:26px;background:var(--ink)}
  .holder__name{color:var(--accent);font-weight:600;font-size:19px;line-height:1.1}
  .holder__role{font-size:11px;color:var(--muted);margin-top:2px}
  .contact{
    position:absolute;left:22px;right:16px;top:160px;
    display:flex;align-items:flex-start;font-size:11.5px;color:var(--muted);
  }
  .contact__group{padding:2px 14px;border-left:1px solid var(--rule);white-space:nowrap}
  .contact__group:first-child{border-left:none;padding-left:0}
  .contact__line{display:flex;align-items:center;gap:7px;line-height:20px}
  .contact__line svg{width:11px;height:11px;fill:var(--ink);flex:none}
  .contact__line--address{align-items:flex-start}
  .contact__line--address svg{margin-top:4px}
  .card--back .brand{position:absolute;left:50%;top:50%;transform:translate(-50%,-58%)}
  .card--back .brand-name{font-size:46px}
  .slogan{font-size:11px;color:var(--muted);margin-top:8px}
</style>
</head>
<body>
  <section class="card card--front" aria-label="Business card front">
    <div class="holder">
      <span class="holder__marker"></span>
      <div class="holder__name">QR-TOP</div>
      <div class="holder__role">President</div>
    </div>
    <div class="brand-name">QR-TOP</div>
    <div class="contact">
      <div class="contact__group">
        <div class="contact__line"><svg viewBox="0 0 24 24"><path d="M6.6 10.8a15.1 15.1 0 006.6 6.6l2.2-2.2a1 1 0 011-.25 11.4 11.4 0 003.6.57 1 1 0 011 1V20a1 1 0 01-1 1A17 17 0 013 4a1 1 0 011-1h3.5a1 1 0 011 1c0 1.25.2 2.45.57 3.57a1 1 0 01-.25 1z"/></svg>(555) 014-2270</div>
        <div class="contact__line"><svg viewBox="0 0 24 24"><path d="M5 3h14v6H5zM3 10h18v8h-3v3H6v-3H3zm5 5v4h8v-4z"/></svg>(555) 014-3381</div>
      </div>
      <div class="contact__group">
        <div class="contact__line"><svg viewBox="0 0 24 24"><path d="M2 5h20v14H2zm2 2v.5l8 5 8-5V7zm0 3v7h16v-7l-8 5z"/></svg>info@qr-top.com</div>
        <div class="contact__line"><svg viewBox="0 0 24 24"><circle cx="12" cy="12" r="10"/></svg>www.qr-top.com</div>
      </div>
      <div class="contact__group">
        <div class="contact__line contact__line--address"><svg viewBox="0 0 24 24"><path d="M12 3l10 9h-3v9h-5v-6h-4v6H5v-9H2z"/></svg><span>Suite 102, Street name,<br>State, Zip 2034, Country</span></div>
      </div>
    </div>
  </section>

  <section class="card card--back" aria-label="Business card back">
    <div class="brand">
      <div class="brand-name">QR-TOP</div>
      <div class="slogan">Your Slogan here..........</div>
    </div>
  </section>
</body>
</html>
```